Business Card Design Project

Lumen Clinic Group

Dr Tomas Feldren M.D, F.R.C.S
Vascular and Vein Surgery

18-46 Corbell Avenue, Suite 317
Astoria
NY 11290

212-555-0163
718-555-0147
www.palemedic.example back of the card for scheduled appointments up to 5 appointment dates

Target Market(s)

Male and Female patients from 25 onwards with spider veins or varicose veins

Industry/Entity Type

Business

Font styles to use
Serif

Colors
86cae6
85abd2
0456a4

Requirements
Must have
• Modern Sophisticated design using light blue and grey text
Should not have
• hearts or flowers

```html
<!DOCTYPE html>
<html lang="en">
<head>
<meta charset="utf-8">
<title>Lumen Clinic Group – Business Card</title>
<link rel="stylesheet" href="https://fonts.googleapis.com/css2?family=EB+Garamond:wght@400;500;600&display=swap">
<style>
  :root {
    --blue-deep: #0456a4;
    --blue-mid: #85abd2;
    --blue-light: #86cae6;
    --grey-text: #3d3f42;
    --grey-soft: #6b6d70;
    --grey-band: #3a3c40;
    --page: #e9eaec;
    --card-light: #f6f4f2;
    --skin: #efe3d8;
  }
  * { box-sizing: border-box; margin: 0; padding: 0; }
  html, body { width: 1200px; height: 1023px; overflow: hidden; }
  body {
    background: var(--page);
    font-family: "EB Garamond", "Palatino Linotype", Georgia, serif;
    position: relative;
  }
  .card {
    position: absolute;
    left: 250px;
    width: 700px;
    height: 400px;
    background: var(--card-light);
    box-shadow: 0 6px 22px rgba(0,0,0,.18);
    overflow: hidden;
  }
  .card--back { top: 60px; }
  .card--front { top: 540px; }

  /* Back side */
  .back-panel {
    position: absolute; left: 0; top: 0; width: 250px; height: 100%;
    background: linear-gradient(160deg, #1a72c0 0%, var(--blue-deep) 70%, #034a8e 100%);
    color: #fff; text-align: center;
    display: flex; flex-direction: column; justify-content: center; gap: 26px;
    font-size: 17px; line-height: 1.35;
  }
  .back-photo {
    position: absolute; left: 250px; top: 0; right: 0; bottom: 0;
    background: linear-gradient(135deg, #ffffff 0%, var(--card-light) 40%, var(--skin) 75%, #e6e4e6 100%);
  }
  .back-content { position: absolute; left: 290px; top: 34px; right: 40px; }
  .clinic-name--back {
    font-size: 36px; font-weight: 500; color: var(--grey-text);
    text-align: center; line-height: 1;
  }
  .schedule-title {
    text-align: center; color: var(--blue-deep); font-size: 18px; margin-top: 10px;
  }
  .schedule { margin-top: 38px; display: flex; flex-direction: column; gap: 22px; }
  .schedule-row { display: flex; align-items: baseline; font-size: 15px; color: var(--grey-soft); }
  .schedule-row .label { margin-right: 4px; }
  .schedule-row .dots { flex: 1; border-bottom: 1px dotted #9a9c9f; margin-right: 10px; }
  .schedule-row .dots:last-child { margin-right: 0; }

  /* Front side */
  .front-photo {
    position: absolute; inset: 0;
    background: radial-gradient(ellipse at 78% 38%, var(--skin) 0%, #f3ebe4 35%, #f7f6f5 65%, #fbfbfb 100%);
  }
  .clinic-name--front {
    position: absolute; left: 40px; top: 76px;
    font-size: 60px; font-weight: 500; color: var(--grey-text); line-height: 1;
  }
  .doctor { position: absolute; right: 52px; top: 196px; text-align: right; line-height: 1.2; }
  .doctor-name { color: var(--blue-deep); font-size: 20px; font-weight: 600; }
  .doctor-role { color: var(--grey-text); font-size: 15.5px; }
  .divider { position: absolute; left: 40px; top: 238px; width: 410px; height: 1px; background: #7d7f82; }
  .contact { position: absolute; left: 40px; top: 246px; color: var(--grey-text); font-size: 15.5px; line-height: 22px; }
  .contact-list { list-style: none; margin-top: 8px; }
  .contact-list li { display: flex; align-items: center; gap: 8px; height: 22px; font-size: 16px; }
  .contact-list svg { width: 15px; height: 15px; flex: none; }
  .band { position: absolute; left: 0; bottom: 0; width: 100%; height: 18px; }
</style>
</head>
<body>

<section class="card card--back" aria-label="Card back: appointment schedule">
  <div class="back-photo" role="img" aria-label="Soft photo of a laser vein treatment on a patient's leg"></div>
  <div class="back-panel">
    <p class="back-address">18-46 Corbell Avenue, Suite 317<br>Astoria, NY 11290</p>
    <p class="back-hours">Opening hours<br>Monday to Saturday<br>9:00am to 5:00pm</p>
  </div>
  <div class="back-content">
    <h2 class="clinic-name--back">Lumen Clinic Group</h2>
    <p class="schedule-title">Your Appointment Schedule</p>
    <div class="schedule">
      <div class="schedule-row"><span class="label">Date</span><span class="dots"></span><span class="label">Time</span><span class="dots"></span></div>
      <div class="schedule-row"><span class="label">Date</span><span class="dots"></span><span class="label">Time</span><span class="dots"></span></div>
      <div class="schedule-row"><span class="label">Date</span><span class="dots"></span><span class="label">Time</span><span class="dots"></span></div>
      <div class="schedule-row"><span class="label">Date</span><span class="dots"></span><span class="label">Time</span><span class="dots"></span></div>
      <div class="schedule-row"><span class="label">Date</span><span class="dots"></span></div>
    </div>
  </div>
</section>

<section class="card card--front" aria-label="Card front">
  <div class="front-photo" role="img" aria-label="Soft photo of a hand guiding a laser fibre over a patient's leg"></div>
  <h1 class="clinic-name--front">Lumen Clinic Group</h1>
  <div class="doctor">
    <p class="doctor-name">Dr Tomas Feldren M.D, F.R.C.S</p>
    <p class="doctor-role">Vascular and Vein Surgery</p>
  </div>
  <div class="divider"></div>
  <div class="contact">
    <p class="address">18-46 Corbell Avenue, Suite 317,<br>Astoria NY 11290</p>
    <ul class="contact-list">
      <li>
        <svg viewBox="0 0 16 16" aria-hidden="true"><circle cx="8" cy="8" r="8" fill="#0456a4"/><path d="M4 6.5c0-1 .8-1.6 4-1.6s4 .6 4 1.6l-1.4.5-.5-1H5.9l-.5 1zM5 8h6l.6 3.5H4.4z" fill="#fff"/></svg>
        212-555-0163
      </li>
      <li>
        <svg viewBox="0 0 16 16" aria-hidden="true"><circle cx="8" cy="8" r="8" fill="#0456a4"/><rect x="5.5" y="3.5" width="5" height="9" rx="1" fill="none" stroke="#fff" stroke-width="1.2"/></svg>
        718-555-0147
      </li>
      <li>
        <svg viewBox="0 0 16 16" aria-hidden="true"><circle cx="8" cy="8" r="8" fill="#0456a4"/><g fill="none" stroke="#fff" stroke-width="0.9"><circle cx="8" cy="8" r="4.5"/><ellipse cx="8" cy="8" rx="2" ry="4.5"/><path d="M3.5 8h9"/></g></svg>
        www.palemedic.example
      </li>
    </ul>
  </div>
  <svg class="band" viewBox="0 0 700 18" preserveAspectRatio="none" aria-hidden="true">
    <polygon points="0,0 282,0 276,18 0,18" fill="#0456a4"/>
    <polygon points="284,0 700,0 700,18 278,18" fill="#3a3c40"/>
  </svg>
</section>

</body>
</html>
```